MARLOWE THREADWORK WEB DESIGN PROJECT

We are a brand new company called "Marlowe Threadwork" which specialise in one-off Vintage Clothing. We would like somebody to design a web page which will be the sole income for our company. Our main aim is to have an easy searchable website which is user friendly. The key to the website is to target people who do not like the idea of op-shopping but love vintage clothes - this website will be the answer.
Updates

This website will need to be coded to work with Halvo Shopdesk - Please read this before you start. https://help.halvoshopdesk.example/articles/Public/How-do-I-create-custom-template-files-for-my-store

Hi everyone, Just want to make note that the this website is for young people. Just so people a clear I want modern young people dressed in Vintage clothes as this is that reality and what they would like to see. Not people dressed like they are going to a fancy dress party, i.e. dresses like it was that era. Thanks Rosalind

Coding

Coded - Design and coding required

```html
<!DOCTYPE html>
<html lang="en">
<head>
<meta charset="utf-8">
<title>Marlowe Threadwork — Vintage Clothing</title>
<link href="https://fonts.googleapis.com/css2?family=Ubuntu:wght@400;500;700&display=swap" rel="stylesheet">
<style>
:root{
  --plum:#9a5a93;
  --plum-dark:#7d4477;
  --plum-soft:#b27aab;
  --band:#ecd9ea;
  --band-light:#f7eef6;
  --ink:#2b2b2b;
  --muted:#6a6a6a;
  --header:#f5f5f5;
  --charcoal:#3a3434;
  --white:#ffffff;
}
*{box-sizing:border-box;margin:0;padding:0}
html,body{width:781px;height:1200px;overflow:hidden;background:var(--white)}
body{position:relative;font-family:'Ubuntu',sans-serif;color:var(--ink)}
.abs{position:absolute}
a{color:inherit;text-decoration:none}

/* header */
.site-header{left:0;top:0;width:781px;height:71px;background:var(--header)}
.brand{left:130px;top:14px;display:flex;align-items:center;gap:8px}
.brand-mark{width:14px;height:14px;border-radius:50%;background:var(--plum)}
.brand-name{font-size:19px;font-weight:700;color:var(--plum);line-height:1.05;width:130px}
.util-link{top:8px;display:flex;align-items:center;gap:5px;font-size:8.5px;color:#555}
.util-icon{width:14px;height:14px;background:var(--plum);display:flex;align-items:center;justify-content:center}
.search{left:298px;top:40px;width:209px;height:17px;border:1px solid #bbb;background:#fff;font-size:7.5px;color:#999;padding:4px 6px}
.search-btn{left:485px;top:40px;width:22px;height:17px;background:#555;display:flex;align-items:center;justify-content:center}
.btn-small{top:40px;height:16px;font-size:8.5px;font-weight:500;color:#fff;display:flex;align-items:center;justify-content:center}
.signup{left:554px;width:45px;background:var(--plum)}
.login{left:606px;width:45px;background:#3d3d3d}

/* nav */
.main-nav{left:0;top:71px;width:781px;height:24px;background:var(--plum)}
.nav-item{top:0;height:24px;display:flex;align-items:center;gap:5px;color:#fff;font-size:10.5px;font-weight:500}
.nav-sep{top:0;width:1px;height:24px;background:rgba(255,255,255,.18)}

/* hero */
.hero-photo{left:0;top:95px;width:781px;height:261px;background:linear-gradient(90deg,#f3eced 0%,#e7b8bd 18%,#f5f2f2 32%,#3a3536 48%,#e9e6e6 62%,#f4f2f2 78%,#2f2b2d 90%,#f6f4f4 100%)}
.hero-arrow{top:210px;width:31px;height:31px;background:var(--plum);display:flex;align-items:center;justify-content:center}
.hero-arrow.next{background:var(--plum-soft)}
.hero-panel{left:189px;top:181px;width:403px;height:109px;background:rgba(70,70,70,.72);text-align:center;color:#fff}
.hero-panel p{font-size:17.5px;line-height:22px;margin-top:17px}
.hero-cta{display:inline-block;margin-top:10px;background:var(--plum);padding:4px 7px;font-size:10.5px;font-weight:500}

/* featured */
.featured{left:0;top:356px;width:781px;height:210px;background:linear-gradient(90deg,var(--band) 0%,var(--band-light) 50%,var(--band) 100%)}
.section-title{font-size:15px;font-weight:500;color:var(--ink)}
.product{top:406px;width:111px}
.product-photo{width:111px;height:90px;border:1.5px solid var(--plum)}
.price{position:absolute;right:-8px;top:-7px;width:30px;height:30px;border-radius:50%;background:var(--plum);color:#fff;font-size:9.5px;font-weight:500;display:flex;align-items:center;justify-content:center}
.product-name{font-size:7.5px;font-weight:500;text-align:center;margin-top:8px}
.add-cart{display:block;width:61px;height:18px;margin:7px auto 0;background:var(--plum);color:#fff;font-size:7.5px;font-weight:500;text-align:center;line-height:18px}

/* promo boxes */
.promo{top:584px;width:149px;height:226px;color:#fff;padding:10px 12px}
.promo-tips{left:130px;background:linear-gradient(160deg,#b887b2,#a06d9a 60%,#b58db0)}
.promo-era{left:316px;background:linear-gradient(160deg,#4a4242,#342e2e 60%,#4d4444)}
.promo-vip{left:502px;background:linear-gradient(160deg,#b685b1,#a36f9e 55%,#c198bc)}
.promo h3{font-size:12.5px;font-weight:500;padding-bottom:5px;border-bottom:1px solid rgba(255,255,255,.6)}
.tick-list{list-style:none;margin-top:7px}
.tick-list li{font-size:10px;line-height:21.6px;display:flex;align-items:center;gap:4px}
.era-text{font-size:7.5px;line-height:12px;margin-top:8px}
.read-more{position:absolute;right:12px;bottom:10px;background:var(--plum);font-size:9.5px;font-weight:500;padding:4px 5px}
.promo-tips .read-more,.promo-vip .join{background:#4a3e44}
.vip-title{font-size:12.5px;font-weight:500;line-height:17.5px}
.field-label{font-size:7px;margin-top:7px}
.field{height:17px;background:#fff;margin-top:5px}
.join{position:absolute;right:12px;bottom:10px;font-size:9.5px;font-weight:500;padding:4px 10px}

/* quote */
.quote-mark{font-size:34px;color:#d6b4d2;font-weight:700;line-height:1}
.quote{left:170px;top:837px;width:441px;text-align:center;font-size:9.5px;font-weight:500;color:var(--plum);line-height:17.6px}

/* community */
.community{left:0;top:890px;width:781px;height:111px;background:linear-gradient(90deg,var(--band) 0%,var(--band-light) 55%,var(--band) 100%)}
.newsletter-input{left:130px;top:958px;width:202px;height:21px;border:1px solid var(--plum);background:#fff;font-size:7.5px;color:#777;padding:6px 6px}
.subscribe{left:331px;top:958px;width:59px;height:21px;background:var(--plum);color:#fff;font-size:7.5px;font-weight:500;display:flex;align-items:center;justify-content:center}
.social{top:932px;width:60px;text-align:center;font-size:7.5px;font-weight:500}
.social-dot{width:34px;height:34px;border-radius:50%;margin:8px auto 0}

/* footer */
.footer-col h4{font-size:10.5px;font-weight:500;margin-bottom:6px}
.footer-col li{list-style:none;font-size:8px;color:#555;line-height:17.6px}
.footer-divider{top:1012px;width:1px;height:150px;background:#ececec}
.pay-badge{top:1120px;height:16px;border:1px solid #ccc}
.bottom-bar{left:0;top:1166px;width:781px;height:34px;background:var(--plum);color:#fff;font-size:7.5px;display:flex;align-items:center;justify-content:center}
</style>
</head>
<body>

<header class="abs site-header">
  <div class="abs brand" style="left:130px;top:12px">
    <span class="brand-mark"></span>
    <span class="brand-name">Marlowe Threadwork</span>
  </div>
  <a class="abs util-link" style="left:436px"><span class="util-icon"><svg width="9" height="8" viewBox="0 0 9 8"><path d="M0 1h2l1 4h5l1-3H2.5" fill="none" stroke="#fff" stroke-width="1"/><circle cx="3.5" cy="7" r=".8" fill="#fff"/><circle cx="7" cy="7" r=".8" fill="#fff"/></svg></span>Add to cart</a>
  <a class="abs util-link" style="left:518px"><span class="util-icon"><svg width="8" height="7" viewBox="0 0 8 7"><path d="M4 7L.5 3.3A1.8 1.8 0 0 1 4 1.3a1.8 1.8 0 0 1 3.5 2z" fill="#fff"/></svg></span>My Wishlist</a>
  <a class="abs util-link" style="left:606px"><span class="util-icon" style="color:#fff;font-size:9px;font-weight:700">?</span>Help</a>
  <div class="abs search">Search your product...</div>
  <div class="abs search-btn"><svg width="9" height="9" viewBox="0 0 9 9"><circle cx="3.6" cy="3.6" r="2.7" fill="none" stroke="#fff" stroke-width="1.2"/><path d="M5.6 5.6L8.5 8.5" stroke="#fff" stroke-width="1.3"/></svg></div>
  <a class="abs btn-small signup">Sign Up</a>
  <a class="abs btn-small login">Login</a>
</header>

<nav class="abs main-nav">
  <a class="abs nav-item" style="left:130px"><svg width="11" height="10" viewBox="0 0 11 10"><path d="M5.5 0L0 5h1.5v5h3V7h2v3h3V5H11z" fill="#fff"/></svg>Home</a>
  <span class="abs nav-sep" style="left:186px"></span>
  <a class="abs nav-item" style="left:198px"><svg width="10" height="11" viewBox="0 0 10 11"><circle cx="5" cy="3" r="2.6" fill="#fff"/><path d="M0 11c0-4 2-5 5-5s5 1 5 5z" fill="#fff"/></svg>Men</a>
  <span class="abs nav-sep" style="left:249px"></span>
  <a class="abs nav-item" style="left:261px"><svg width="10" height="11" viewBox="0 0 10 11"><circle cx="5" cy="3" r="2.6" fill="#fff"/><path d="M0 11c0-4 2-5 5-5s5 1 5 5z" fill="#fff"/></svg>Women</a>
  <span class="abs nav-sep" style="left:321px"></span>
  <span class="abs nav-sep" style="left:520px"></span>
  <a class="abs nav-item" style="left:532px"><svg width="8" height="11" viewBox="0 0 8 11"><circle cx="4" cy="4" r="3.6" fill="#fff"/><rect x="2.5" y="7.5" width="3" height="3" fill="#fff"/></svg>Style Tips</a>
  <span class="abs nav-sep" style="left:602px"></span>
  <a class="abs nav-item" style="left:614px"><span style="font-size:13px;font-weight:700">?</span>&nbsp;FAQ</a>
</nav>

<section>
  <div class="abs hero-photo" role="img" aria-label="Three young women in polka-dot vintage dresses posing on a white background"></div>
  <a class="abs hero-arrow" style="left:124px"><svg width="10" height="16" viewBox="0 0 10 16"><path d="M8 1L2 8l6 7" fill="none" stroke="#fff" stroke-width="2"/></svg></a>
  <a class="abs hero-arrow next" style="left:626px"><svg width="10" height="16" viewBox="0 0 10 16"><path d="M2 1l6 7-6 7" fill="none" stroke="#fff" stroke-width="2"/></svg></a>
  <div class="abs hero-panel">
    <p>Orders over $100 will receive FREE shipping!<br>Find out more about delivery &amp; shipping</p>
    <a class="hero-cta">LEARN MORE</a>
  </div>
</section>

<section>
  <div class="abs featured"></div>
  <h2 class="abs section-title" style="left:130px;top:374px">Featured Products</h2>

  <div class="abs product" style="left:130px">
    <div class="product-photo" role="img" aria-label="Cream floral 1950s party dress on a mannequin" style="background:linear-gradient(180deg,#8c9da6,#d9d3c6 60%,#7f8f94)"></div>
    <span class="price">$25</span>
    <p class="product-name">1950s Party Dress</p>
    <a class="add-cart">ADD TO CART</a>
  </div>
  <div class="abs product" style="left:265px">
    <div class="product-photo" role="img" aria-label="Camel double breasted coat" style="background:linear-gradient(180deg,#fff,#c9a98a 40%,#b08d6c 80%,#fff)"></div>
    <span class="price">$30</span>
    <p class="product-name">Double Breasted Coat</p>
    <a class="add-cart">ADD TO CART</a>
  </div>
  <div class="abs product" style="left:397px">
    <div class="product-photo" role="img" aria-label="Patterned 1960s hippy dress with lace collar" style="background:linear-gradient(180deg,#fff,#6a4a3a 35%,#3d2c3a 75%,#fff)"></div>
    <span class="price">$25</span>
    <p class="product-name">1960s Hippy Dress</p>
    <a class="add-cart">ADD TO CART</a>
  </div>
  <div class="abs product" style="left:532px">
    <div class="product-photo" role="img" aria-label="Printed 1980s high waisted pants" style="background:linear-gradient(180deg,#fff,#3d6f7d 30%,#2e4f63 80%,#fff)"></div>
    <span class="price">$35</span>
    <p class="product-name">1980s High Pant</p>
    <a class="add-cart">ADD TO CART</a>
  </div>
</section>

<section>
  <div class="abs promo promo-tips" role="img" aria-label="Tinted photo of a woman in a vintage dress behind the style tips">
    <h3>Style Tips</h3>
    <ul class="tick-list">
      <li><span>✓</span>Lorem Ipsum is simply</li>
      <li><span>✓</span>dummy text of the</li>
      <li><span>✓</span>printing and typeset-</li>
      <li><span>✓</span>ting industry. Lorem</li>
      <li><span>✓</span>Ipsum has been the</li>
      <li><span>✓</span>industry's standard</li>
      <li><span>✓</span>dummy text ever since</li>
    </ul>
    <a class="read-more">Read More</a>
  </div>
  <div class="abs promo promo-era">
    <h3>Shop Era</h3>
    <p class="era-text">Lorem Ipsum is simply dummy text of the printing and typesetting industry. Lorem Ipsum has been the industry's standard dummy text ever since the 1500s, when an unknown printer took a galley of type and scrambled it to make a type specimen book. It has survived not only five centuries, but also the leap into electronic typesetting, remaining essentially unchanged.......</p>
    <a class="read-more">Read More</a>
  </div>
  <div class="abs promo promo-vip" role="img" aria-label="Tinted photo of a smiling shopper with bags behind the sign-up form">
    <p class="vip-title">Join our VIP club and receive 5% off every order!</p>
    <p class="field-label" style="margin-top:9px">Your Name</p><div class="field"></div>
    <p class="field-label">Email ID</p><div class="field"></div>
    <p class="field-label">Mobile Number</p><div class="field"></div>
    <a class="join">Join Now</a>
  </div>
</section>

<section>
  <span class="abs quote-mark" style="left:130px;top:832px">&ldquo;</span>
  <p class="abs quote">Marlowe Threadwork is all about being different. That's way all of our clothes are unique, so you can dazzling different</p>
  <span class="abs quote-mark" style="left:629px;top:858px">&rdquo;</span>
</section>

<section>
  <div class="abs community"></div>
  <h2 class="abs section-title" style="left:130px;top:902px;font-size:16.5px">Become part of our community</h2>
  <p class="abs" style="left:130px;top:932px;font-size:10px;font-weight:500">Sign up to our newsletter</p>
  <div class="abs newsletter-input">Enter Your Email</div>
  <a class="abs subscribe">SUBSCRIBE</a>

  <h2 class="abs section-title" style="left:450px;top:902px;font-size:16.5px">Follow Us On</h2>
  <a class="abs social" style="left:437px">Circlefeed<div class="social-dot" style="background:#3a5797"></div></a>
  <a class="abs social" style="left:491px">Pinboard Lane<div class="social-dot" style="background:#c8202a"></div></a>
  <a class="abs social" style="left:544px">Snapframe<div class="social-dot" style="background:#6b5c50"></div></a>
  <a class="abs social" style="left:598px">Blog<div class="social-dot" style="background:#f07d1a"></div></a>
</section>

<footer>
  <div class="abs footer-col" style="left:161px;top:1024px">
    <h4>Marlowe Threadwork</h4>
    <ul><li>About Us</li><li>Terms of use</li><li>Privacy policy</li><li>Press</li></ul>
  </div>
  <span class="abs pay-badge" style="left:161px;width:25px;background:#eef0f6"></span>
  <span class="abs pay-badge" style="left:188px;width:25px;background:#f4e6d8"></span>
  <span class="abs pay-badge" style="left:215px;width:25px;background:#e3ebf5"></span>
  <span class="abs pay-badge" style="left:243px;width:67px;background:#f3f3f3"></span>
  <span class="abs footer-divider" style="left:329px"></span>
  <div class="abs footer-col" style="left:356px;top:1024px">
    <h4>Connect With Us</h4>
    <ul><li>Contact Us</li><li>My Account</li><li>Style Tips</li><li>FAQ's</li><li>Shipping</li><li>Track Your Order</li><li>Size Chart</li></ul>
  </div>
  <span class="abs footer-divider" style="left:459px"></span>
  <div class="abs footer-col" style="left:480px;top:1024px">
    <h4>Shop By Popular Categories</h4>
    <ul><li>Men</li><li>Women</li><li>Accessories</li><li>Bags</li><li>Shoes</li></ul>
  </div>
  <div class="abs footer-col" style="left:555px;top:1041px">
    <ul><li>50s</li><li>60s</li><li>70s</li><li>80s</li><li>90s</li></ul>
  </div>
  <div class="abs bottom-bar">All Rights Reserved © Marlowe Threadwork. All Prices are in AUD.</div>
</footer>

</body>
</html>
```